étiquette 4.5 sur 12.5 cm pour shampooing pour chiens Ostrafel

Étiquette pour six shampooings et un bain crème
produits destinés aux particuliers et distribués dans les animaleries;
retour à la formulation américaine initiale.
adaptable sur un flacon rond, partie visible de face cinq centimètres sur douze centimètres et demi de hauteur.
nous désirons une étiquette sur un fond de couleur pour pouvoir différencier visuellement et instantanément les différents produits.
le flacon est rond et de couleur blanche , l'étiquette recouvrira la presque totalité de ce flacon . l'étiquette totale est quatorze centimètres et 80milimètres

Target Market(s)

clients particuliers, produits distribués en animaleries

Font styles to use
Sans Serif

Requirements
Must have
• le nom OSTRAFEL en gras , puis PET CARE en plus petit
le type de produits ex: WHITE COAT SHAMPOO
l'explication du produit en 2 langues ex: shampooing chiens blancs
un dessin de chien
Nice to have
• un fond de couleur
un dessin de chien stylisé ou humoristique

```html
<!DOCTYPE html>
<html lang="fr">
<head>
<meta charset="utf-8">
<title>Ostrafel Pet Care – White Coat Shampoo</title>
<link rel="stylesheet" href="https://fonts.googleapis.com/css2?family=Sniglet:wght@400;800&display=swap">
<style>
  :root {
    --backdrop: #b4b5b6;
    --label-white: #f3f4f3;
    --label-teal: #5b92a4;
    --teal-deep: #4b8093;
    --ink: #3b474c;
  }
  html, body {
    margin: 0;
    padding: 0;
    width: 1200px;
    height: 720px;
    overflow: hidden;
    background: var(--backdrop);
  }
  .canvas {
    width: 1200px;
    height: 720px;
    display: flex;
    align-items: center;
    justify-content: center;
  }
  .label {
    width: 400px;
    height: 640px;
    display: block;
    font-family: "Sniglet", sans-serif;
  }
  .label-paper { fill: var(--label-white); }
  .label-field { fill: var(--label-teal); }
  .foam-dot { fill: var(--label-white); }
  .brand-bubble { fill: var(--label-white); }
  .brand-name {
    fill: var(--label-teal);
    font-weight: 800;
    font-size: 34px;
  }
  .brand-tagline {
    fill: var(--ink);
    font-weight: 800;
    font-size: 17px;
    letter-spacing: 1px;
  }
  .mascot-area { fill: var(--teal-deep); }
  .product-type {
    fill: var(--label-white);
    font-weight: 800;
    font-size: 20px;
  }
  .foam-cloud { fill: var(--label-white); }
  .product-description {
    fill: var(--ink);
    font-weight: 800;
    font-size: 22px;
  }
</style>
</head>
<body>
<main class="canvas">
  <svg class="label" viewBox="0 0 400 640" xmlns="http://www.w3.org/2000/svg" aria-label="Étiquette Ostrafel Pet Care, White Coat Shampoo">
    <defs>
      <path id="description-curve" d="M18 528 C 150 508, 300 536, 372 640"/>
    </defs>

    <rect class="label-paper" x="0" y="0" width="400" height="640"/>

    <path class="label-field" d="M0 60 C 60 40, 110 70, 170 55 C 240 38, 320 70, 400 50 L400 560 L0 560 Z"/>

    <circle class="foam-dot" cx="70" cy="330" r="12"/>
    <circle class="foam-dot" cx="18" cy="382" r="9"/>
    <circle class="foam-dot" cx="20" cy="470" r="24"/>
    <circle class="foam-dot" cx="300" cy="530" r="9"/>

    <g class="brand" transform="rotate(-10 160 175)">
      <rect class="brand-bubble" x="25" y="118" width="270" height="112" rx="50"/>
      <path class="brand-bubble" d="M200 220 L232 256 L240 214 Z"/>
      <text class="brand-name" x="160" y="174" text-anchor="middle">OSTRAFEL</text>
      <text class="brand-tagline" x="175" y="202" text-anchor="middle">PET CARE</text>
    </g>

    <rect class="mascot-area" x="200" y="250" width="160" height="180" rx="40" role="img" aria-label="Dessin humoristique d'un chiot blanc assis et souriant"/>

    <text class="product-type" x="218" y="476" text-anchor="middle">WHITE COAT SHAMPOO</text>

    <path class="foam-cloud" d="M0 520 C 40 490, 90 520, 130 500 C 180 478, 230 520, 280 505 C 330 490, 370 540, 400 520 L400 640 L0 640 Z"/>

    <text class="product-description">
      <textPath href="#description-curve">shampooing chiens blancs</textPath>
    </text>
  </svg>
</main>
</body>
</html>
```